Marcelo Quintana Postcard/Rack Card

Marcelo Quintana
Tenor & Vocal Coach
mqvoice@brivamail.com
(713) 582-6031
www.voicefromthecore.com
Want two sided postcard / rack card.4" x 9"
Front - vertical - picture in t-shirt, name, title (Tenor & Vocal Coach), contact information
Back - horizontal - picture in jacket, name, title (Tenor & Vocal Coach), contact information, bio (see attachment for words)
Do not leave space for an address.
Looking for an edgy modern design!

Target Market(s)

Young adults

Requirements
Nice to have
• Will pay extra to get a complimentary business card design, two sided

```html
<!DOCTYPE html>
<html lang="en">
<head>
<meta charset="utf-8">
<title>Marcelo Quintana – Rack Card</title>
<link href="https://fonts.googleapis.com/css2?family=Francois+One&family=Roboto:wght@400&family=Lato:ital,wght@1,400&family=Courgette&display=swap" rel="stylesheet">
<style>
:root{
  --bg:#e9e6e1;
  --dark:#2e2e2e;
  --dark-2:#3f3f3f;
  --orange:#ee7a1d;
  --orange-deep:#e0601a;
  --blue:#1f73c9;
  --blue-deep:#1859a8;
  --white:#ffffff;
  --photo-a:#c9c3b6;
  --photo-b:#8e8a86;
}
*{margin:0;padding:0;box-sizing:border-box}
html,body{width:825px;height:1200px;overflow:hidden;background:var(--bg)}
body{position:relative;font-family:'Roboto',Arial,sans-serif}

/* ---------- front (vertical) ---------- */
.rack-front{position:absolute;left:268px;top:110px;width:289px;height:578px;overflow:hidden;background:var(--dark);box-shadow:0 2px 6px rgba(0,0,0,.25)}
.rack-front .portrait{position:absolute;left:0;top:0;width:289px;height:390px;background:radial-gradient(ellipse at 50% 40%,var(--photo-a),var(--photo-b))}
.rack-front .wave{position:absolute;left:0;top:0;width:289px;height:578px}
.rack-front .name{position:absolute;left:35px;top:398px;font-family:'Francois One',Impact,sans-serif;font-size:26px;color:var(--white);letter-spacing:.3px}
.contact-list{list-style:none;position:absolute}
.rack-front .contact-list{left:34px;top:438px}
.rack-front .contact-list li{display:flex;align-items:center;height:26px;font-size:20px;color:var(--white)}
.icon{display:inline-block;flex:none;border-radius:50%;background:var(--blue);border:1.5px solid var(--white)}
.rack-front .icon{width:18px;height:18px;margin-right:9px}
.rack-front .web-band{position:absolute;left:0;bottom:0;width:289px;height:43px;background:linear-gradient(var(--orange),var(--orange-deep));display:flex;align-items:center;justify-content:center;color:var(--white);font-size:12px;letter-spacing:2.4px}

/* ---------- back (horizontal) ---------- */
.rack-back{position:absolute;left:124px;top:766px;width:577px;height:289px;overflow:hidden;background:var(--dark);box-shadow:0 2px 6px rgba(0,0,0,.25)}
.rack-back .portrait{position:absolute;left:0;top:0;width:164px;height:182px;background:radial-gradient(ellipse at 50% 40%,#d8d0b8,#6f7280)}
.rack-back .id-panel{position:absolute;left:0;top:182px;width:164px;height:107px;background:linear-gradient(135deg,var(--orange-deep),var(--orange))}
.rack-back .divider{position:absolute;left:164px;top:0;width:5px;height:289px;background:var(--white)}
.rack-back .name{position:absolute;left:21px;top:14px;font-family:'Francois One',Impact,sans-serif;font-size:15px;color:var(--white)}
.rack-back .contact-list{left:20px;top:37px}
.rack-back .contact-list li{display:flex;align-items:center;height:15.5px;font-size:12px;color:var(--white)}
.rack-back .icon{width:11px;height:11px;margin-right:5px;border-width:1px}
.rack-back .info{position:absolute;left:169px;top:0;width:408px;height:289px;background:linear-gradient(var(--dark-2),var(--dark))}
.rack-back .shapes{position:absolute;left:0;top:0;width:408px;height:289px}
.rack-back .bio{position:absolute;left:21px;top:29px;width:368px;font-family:'Lato',Arial,sans-serif;font-style:italic;font-size:8.6px;line-height:11.8px;color:var(--white)}
.rack-back .script{position:absolute;font-family:'Courgette',cursive;color:var(--white);white-space:nowrap}
.script.first{left:32px;top:156px;font-size:19px}
.script.last{left:67px;top:190px;font-size:24px}
.script.role{left:32px;top:226px;font-size:21px}
.rack-back .score{position:absolute;left:0;top:0;width:408px;height:289px}
</style>
</head>
<body>

<section class="rack-front">
  <div class="portrait" role="img" aria-label="Photo of Marcelo smiling in a grey t-shirt"></div>
  <svg class="wave" viewBox="0 0 289 578" aria-hidden="true">
    <defs>
      <linearGradient id="frontDark" x1="0" y1="0" x2="0" y2="1">
        <stop offset="0" stop-color="#3c3c3c"/><stop offset="1" stop-color="#262626"/>
      </linearGradient>
    </defs>
    <path d="M0,368 C95,364 205,340 289,278 L289,578 L0,578 Z" fill="#fff"/>
    <path d="M0,374 C95,370 205,348 289,290 L289,578 L0,578 Z" fill="var(--orange)"/>
    <path d="M0,380 C95,376 205,356 289,300 L289,578 L0,578 Z" fill="url(#frontDark)"/>
  </svg>
  <h1 class="name">Marcelo Quintana</h1>
  <ul class="contact-list">
    <li><span class="icon"></span>Tenor &amp; Vocal Coach</li>
    <li><span class="icon"></span>mqvoice@brivamail.com</li>
    <li><span class="icon"></span>(713) 582-6031</li>
  </ul>
  <div class="web-band">www.voicefromthecore.com</div>
</section>

<section class="rack-back">
  <div class="portrait" role="img" aria-label="Photo of Marcelo in a dark blazer"></div>
  <div class="id-panel">
    <h2 class="name">Marcelo Quintana</h2>
    <ul class="contact-list">
      <li><span class="icon"></span>Tenor &amp; Vocal Coach</li>
      <li><span class="icon"></span>mqvoice@brivamail.com</li>
      <li><span class="icon"></span>(713) 582-6031</li>
    </ul>
  </div>
  <div class="divider"></div>
  <div class="info">
    <p class="bio">Marcelo is a local singer and actor who has been working professionally around the country as a concert artist and musical theater performer. He studied at the Alder School of Music, Bayou City University and works as a vocal coach with local youths and adults in Houston area. Marcelo's goal is to help his students master their individual instrument so that they can achieve a natural and effortless vocal production.<br>For more information please contact Marcelo today!</p>
    <svg class="shapes" viewBox="0 0 408 289" aria-hidden="true">
      <defs>
        <linearGradient id="backBlue" x1="0" y1="0" x2="1" y2="1">
          <stop offset="0" stop-color="var(--blue)"/><stop offset="1" stop-color="var(--blue-deep)"/>
        </linearGradient>
      </defs>
      <path d="M0,112 C120,140 300,140 408,98 L408,289 L0,289 Z" fill="#fff"/>
      <path d="M0,118 C120,146 300,146 408,108 L408,289 L0,289 Z" fill="var(--blue)"/>
      <path d="M0,124 C120,152 300,152 408,114 L408,289 L0,289 Z" fill="url(#backBlue)"/>
      <polygon points="222,146 408,122 408,289 195,289" fill="var(--orange)"/>
    </svg>
    <svg class="score" viewBox="0 0 408 289" role="img" aria-label="Sheet music background">
      <defs>
        <linearGradient id="sheet" x1="0" y1="0" x2="1" y2="1">
          <stop offset="0" stop-color="#ffffff"/><stop offset="1" stop-color="#d9d9d9"/>
        </linearGradient>
      </defs>
      <polygon points="225,147 408,124 408,289 198,289" fill="url(#sheet)"/>
    </svg>
    <span class="script first">Marcelo</span>
    <span class="script last">Quintana</span>
    <span class="script role">Tenor &amp; Vocal</span>
  </div>
</section>

</body>
</html>
```